The Brawlhaven 2015 All Positions Training Showcase

The Brawlhaven 2015
All Positions Football Training Show Case
Sunday, June 7, 2015
Check In 8 AM - 9 AM
Showcase 9 AM - 11 AM
Fee $65
Open to all 10th, 11th and 12th grades limited to 200 entrants.
Copper Ridge High School Football Stadium
Student Athletes instructed by participating coaches from WSL 9 and Granite Coast
Register and information go to www.ironwaveathletics.example

Target Market(s)

High school student athletes participating in all football positions grades 10, 11 and 12. Open to all students nationwide. Football coaches from Division 1A nationwide.

Industry/Entity Type

Training

Requirements
Must have
• Submitted a flyer from last year as an example. I would like to keep with the same theme. Tough, rough and mean. I need font to reflect toughness as well. Our company colors are black, red and gray. Stay with the company color scheme. Pictures submitted are pictures from our clinics we would like to include some or 2 of the pictures in the flyer. FYI in the past the showcase was for lineman only. But, this year we are including skills players during the showcase. So definitely need to include these players on the flyer if possible. For more information about us visit our website www.ironwaveathletics.example
Nice to have
• It would be nice to have the flyer continue to be personalized towards Iron Wave Athletics' name brand or theme.
Should not have
• Should not be fluffy.

```html
<!DOCTYPE html>
<html lang="en">
<head>
<meta charset="utf-8">
<title>The Brawlhaven 2015 All Positions Training Showcase</title>
<link rel="stylesheet" href="https://fonts.googleapis.com/css2?family=Anton&family=Oswald:wght@400;600;700&display=swap">
<style>
  :root {
    --black: #111214;
    --charcoal: #2a2c2f;
    --gray: #b9bcc0;
    --gray-light: #e4e6e8;
    --red: #d3202a;
    --red-dark: #9e141b;
    --white: #ffffff;
    --turf: #3f7d2e;
    --turf-dark: #1f4417;
  }
  * { margin: 0; padding: 0; box-sizing: border-box; }
  html, body { width: 898px; height: 1200px; overflow: hidden; background: var(--black); }
  .flyer {
    position: relative; width: 898px; height: 1200px; overflow: hidden;
    background: radial-gradient(ellipse at 50% 45%, #3a3c40 0%, #1c1d20 60%, var(--black) 100%);
    font-family: "Oswald", sans-serif; color: var(--white);
  }
  .photo-strip {
    position: absolute; left: 0; top: 0; width: 898px; height: 285px;
    background: linear-gradient(180deg, #6f7d86 0%, #4e6a3c 55%, #2c4a22 100%);
    border-bottom: 4px solid var(--black);
  }
  .headline-row {
    position: absolute; top: 300px; left: 0; width: 898px; height: 200px;
  }
  .headline-side { position: absolute; width: 330px; text-align: center; }
  .headline-side.left { left: 30px; }
  .headline-side.right { right: 30px; }
  .headline-red {
    font-family: "Anton", sans-serif; color: var(--red); font-size: 42px;
    letter-spacing: 1px; line-height: 1; text-transform: uppercase;
  }
  .headline-white {
    font-family: "Anton", sans-serif; color: var(--white); font-size: 66px;
    letter-spacing: 2px; line-height: 1.1; text-transform: uppercase;
  }
  .brand {
    position: absolute; left: 349px; top: 290px; width: 200px; height: 200px;
    display: flex; flex-direction: column; align-items: center; justify-content: center; gap: 10px;
  }
  .brand-mark { width: 70px; height: 70px; border-radius: 50%; background: var(--red); border: 4px solid var(--white); }
  .brand-name {
    font-family: "Oswald", sans-serif; font-weight: 700; font-size: 22px; color: var(--white);
    text-transform: uppercase; text-align: center; line-height: 1.1;
  }
  .event-title {
    position: absolute; top: 505px; left: 0; width: 898px; text-align: center;
    font-family: "Anton", sans-serif; text-transform: uppercase; color: var(--gray-light);
    font-size: 108px; line-height: 1; letter-spacing: 3px;
  }
  .event-year {
    position: absolute; top: 620px; left: 0; width: 898px; text-align: center;
    font-family: "Anton", sans-serif; color: var(--gray); font-size: 96px; line-height: 1; letter-spacing: 4px;
  }
  .venue-band {
    position: absolute; top: 738px; left: 0; width: 898px; height: 56px; background: var(--black);
    display: flex; align-items: center; justify-content: center;
  }
  .venue {
    font-family: "Anton", sans-serif; color: var(--red); font-size: 34px; letter-spacing: 1px; text-transform: uppercase;
  }
  .field {
    position: absolute; top: 794px; left: 0; width: 898px; height: 406px;
    background: linear-gradient(180deg, var(--turf) 0%, var(--turf-dark) 60%, #0f1f0b 100%);
  }
  .ball-area {
    position: absolute; top: 980px; left: 560px; width: 300px; height: 100px;
    background: radial-gradient(ellipse at center, #7a3a1c 0%, rgba(90,40,20,0.4) 55%, rgba(0,0,0,0) 75%);
  }
  .details {
    position: absolute; top: 818px; left: 40px; width: 460px;
    font-weight: 600; font-size: 25px; line-height: 1.22; text-transform: uppercase;
  }
  .schedule {
    position: absolute; top: 820px; left: 530px; width: 330px;
  }
  .schedule-times { background: var(--white); color: var(--black); padding: 14px 20px; }
  .schedule-date { font-family: "Anton", sans-serif; color: var(--red); font-size: 30px; text-transform: uppercase; line-height: 1.15; }
  .schedule-line { font-weight: 700; font-size: 22px; text-transform: uppercase; line-height: 1.3; }
  .schedule-line span { color: var(--red); }
  .fee {
    background: var(--red); color: var(--white); font-family: "Anton", sans-serif;
    font-size: 46px; padding: 6px 20px; text-transform: uppercase; line-height: 1.1;
  }
  .audience {
    position: absolute; top: 1082px; left: 40px; width: 818px;
    font-weight: 600; font-size: 21px; line-height: 1.25; text-transform: uppercase;
  }
</style>
</head>
<body>
<main class="flyer">
  <div class="photo-strip" role="img" aria-label="Photos of linemen and skill players drilling at a football clinic"></div>

  <section class="headline-row">
    <div class="headline-side left">
      <p class="headline-red">All Positions</p>
      <p class="headline-white">Football</p>
    </div>
    <div class="headline-side right">
      <p class="headline-red">Training</p>
      <p class="headline-white">Showcase</p>
    </div>
  </section>

  <div class="brand">
    <span class="brand-mark"></span>
    <p class="brand-name">Iron Wave<br>Athletics</p>
  </div>

  <h1 class="event-title">The Brawlhaven</h1>
  <p class="event-year">2015</p>

  <div class="venue-band"><p class="venue">Copper Ridge High School Football Stadium</p></div>

  <div class="field" role="img" aria-label="Football field turf with a football resting on the grass"></div>
  <div class="ball-area" role="img" aria-label="Football on the turf"></div>

  <p class="details">Open to all 10th, 11th and 12th grades limited to 200 entrants. Student athletes instructed by participating coaches from WSL 9 and Granite Coast. Register and information go to www.ironwaveathletics.example</p>

  <aside class="schedule">
    <div class="schedule-times">
      <p class="schedule-date">Sunday, June 7, 2015</p>
      <p class="schedule-line"><span>Check In</span> 8 AM - 9 AM</p>
      <p class="schedule-line"><span>Showcase</span> 9 AM - 11 AM</p>
    </div>
    <p class="fee">Fee $65</p>
  </aside>

  <p class="audience">High school student athletes participating in all football positions grades 10, 11 and 12 open to all students nationwide. Football coaches from Division 1A nationwide.</p>
</main>
</body>
</html>
```